Supplement Bottle Packaging and Design

We want to rebrand our current health supplements (see below). We do want it to be modern, vibrant and appealing supplement bottles. Very upscale and elegant as it targets primarily women.
NOTE: READ THE ATTACHED WORD DOCUMENT!
Bottle size: We are totally open to the bottle size and shape, as long it's a typical supplement bottle size to handle 90-120 capsules; what we mostly need is new bottle design/packaging. YOU DON’T HAVE TO USE THE CURRENT WHITE BOTTLE SHAPE, BUT ANYTHING MORE MODERN WOULD WORK!
Updates
We need more modern, clean sleek designs to choose from
Look and feel
Each slider illustrates characteristics of the customer's brand and the style your logo design should communicate.

```html
<!DOCTYPE html>
<html lang="en">
<head>
<meta charset="utf-8">
<title>Supplement Label Range</title>
<link href="https://fonts.googleapis.com/css2?family=Archivo+Black&family=Lexend:wght@400;500&display=swap" rel="stylesheet">
<style>
:root{
  --bg:#6e9a98;
  --blue:#2b22f0; --blue-deep:#3a2fc0; --blue-soft:#b9b8ff;
  --green:#1a8c1a; --green-deep:#2f6e2f; --green-soft:#bfe6bf;
  --red:#d71c1c; --red-deep:#a83232; --red-soft:#f1c2c2;
  --purple:#9b2bf0; --purple-deep:#6a35a8; --purple-soft:#e2c3fb;
  --white:#ffffff;
}
*{margin:0;padding:0;box-sizing:border-box}
html,body{width:1200px;height:810px;overflow:hidden}
body{background:var(--bg);font-family:"Lexend",sans-serif;position:relative}
.range{position:absolute;left:0;top:385px;width:1200px;height:264px}
.label{
  position:absolute;top:0;width:222px;height:264px;border-radius:4px;overflow:hidden;
  text-align:center;color:var(--accent);
  background:linear-gradient(to bottom,var(--accent) 0%,var(--soft) 24%,var(--white) 42%,var(--white) 62%,var(--soft) 74%,var(--deep) 100%);
}
.label svg.arc{position:absolute;left:0;top:0;width:222px;height:70px}
.blood{left:94px;--accent:var(--blue);--deep:var(--blue-deep);--soft:var(--blue-soft)}
.hormone{left:358px;--accent:var(--green);--deep:var(--green-deep);--soft:var(--green-soft)}
.tummy{left:622px;--accent:var(--red);--deep:var(--red-deep);--soft:var(--red-soft)}
.liver{left:884px;--accent:var(--purple);--deep:var(--purple-deep);--soft:var(--purple-soft)}
.copy{position:absolute;left:0;right:0;top:68px}
.title{font-family:"Archivo Black",sans-serif;font-size:38px;line-height:40px;letter-spacing:2px}
.subtitle{font-family:"Archivo Black",sans-serif;font-size:17px;line-height:22px;letter-spacing:1px}
.claim{font-size:14px;line-height:16px;margin-top:6px;letter-spacing:1px}
.claim-sub{font-size:10.5px;line-height:12px;letter-spacing:.5px}
.type{font-size:8.5px;margin-top:8px;letter-spacing:.5px}
.count{position:absolute;left:0;right:0;bottom:22px;color:var(--white)}
.count strong{display:block;font-family:"Archivo Black",sans-serif;font-size:12px;line-height:13px}
.count span{font-size:9px;letter-spacing:.5px}
</style>
</head>
<body>
<main class="range">
  <section class="label blood">
    <svg class="arc" viewBox="0 0 222 70" aria-hidden="true"><path d="M0 14 Q111 62 222 14 L222 34 Q111 82 0 34Z" fill="#ffffff" opacity=".55"/></svg>
    <div class="copy">
      <h2 class="title">Blood</h2>
      <p class="subtitle">Sugar Essentials</p>
      <p class="claim">Supports Healthy</p>
      <p class="claim-sub">Blood Glucose Levels</p>
      <p class="type">Dietary Supplement</p>
    </div>
    <p class="count"><strong>60</strong><span>Vegetable Capsules</span></p>
  </section>
  <section class="label hormone">
    <svg class="arc" viewBox="0 0 222 70" aria-hidden="true"><path d="M0 14 Q111 62 222 14 L222 34 Q111 82 0 34Z" fill="#ffffff" opacity=".55"/></svg>
    <div class="copy">
      <h2 class="title" style="font-size:30px">Hormone</h2>
      <p class="subtitle">Essentials</p>
      <p class="claim">Supports Healthy</p>
      <p class="claim-sub">Hormone Levels</p>
      <p class="type">Dietary Supplement</p>
    </div>
    <p class="count"><strong>60</strong><span>Vegetable Capsules</span></p>
  </section>
  <section class="label tummy">
    <svg class="arc" viewBox="0 0 222 70" aria-hidden="true"><path d="M0 14 Q111 62 222 14 L222 34 Q111 82 0 34Z" fill="#ffffff" opacity=".55"/></svg>
    <div class="copy">
      <h2 class="title" style="font-size:34px">Tummy</h2>
      <p class="subtitle">Essentials</p>
      <p class="claim">Oxygenating</p>
      <p class="claim-sub">Colon Cleanse</p>
      <p class="type">Dietary Supplement</p>
    </div>
    <p class="count"><strong>90</strong><span>Vegetable Capsules</span></p>
  </section>
  <section class="label liver">
    <svg class="arc" viewBox="0 0 222 70" aria-hidden="true"><path d="M0 14 Q111 62 222 14 L222 34 Q111 82 0 34Z" fill="#ffffff" opacity=".55"/></svg>
    <div class="copy">
      <h2 class="title">Liver</h2>
      <p class="subtitle">Essentials</p>
      <p class="claim">Rejuvenating</p>
      <p class="claim-sub">Cleanse &amp; Detox Formula</p>
      <p class="type">Dietary Supplement</p>
    </div>
    <p class="count"><strong>120</strong><span>Vegetable Capsules</span></p>
  </section>
</main>
</body>
</html>
```